Progressive business consultancy seeking "Accounting Industry Flyer"

We are looking for an industry flyer that we will use with potential clients/prospects that outlines our skills and experience in delivering change across the Accounting Services Industry. The flyer will be used to help potential clients understand the challenges and issues faced by the accounting industry and how our service offerings can help them solve their project challenges and problems.

About Us:
Based in Melbourne, Australia, Vondra-x is a management consulting organisation that partners with their clients to lead the execution of strategic process and system improvement initiatives.

Vondra-x offers business advisory services in Project Management, Business Process Management, Change Management, Business Analysis and Business Intelligence. Vondra-x combines hands on delivery with coaching in best practice methodologies and approaches to build our clients capabilities ensuring their ongoing success in project implementations.

Vondra-x has extensive experience across a wide range of industries. We specialise in assisting organisations across the accounting, legal, financial services and health sectors.

Our core purpose is to help businesses in the middle market navigate transformational change through clear and focused execution and enablement.

www.vondra-x.com.au
@vondra_x

What we're looking for:

A professional, corporate, industry flyer providing an overview of our capabilities and experience in the accounting industry. Focus is on the "e" in vondra-x. The look should be sharp and crisp, with a professional and corporate feel. The target for the flyer is Accountants and Mid-Tier Accounting Firms.

The Vondra-x colours are white and blue (RGB:0/86/162 and
CMYK 97/73/4/0)

A professional, corporate theme that is consistent across both sides of the flyer. The design should reflect our focus on the "e" in vondra-x, which is what we're really about - "e"xecution and "e"nablement of change.

I've attached a PNG file of our word template which shows the focus on the "e" as a watermark on the document as well as the font files if required.

Let me know if you need any further information or design specifics.

Thanks,

Marisol
(on behalf of Desmond)
Updates

Hi All, Thanks for your design submissions so far. We have discovered that our hero image has not been attached to the brief. Please find the jpeg attached now. It has been loaded as "Vondra-x Hero Image.jpg" Thanks Desmond @vondra_x

Reason: Hi Designers, Thanks to everyone who has taken the time to make a submission on our contest. We really appreciate it. We have decided to extend our deadline by 5 days so we can review the designs with other colleagues and provide feedback to everyone who has made a submission. Thanks for all your creative designs. Desmond @vondra_x

Reason: Hi designers, thanks to everyone for taking the time to submit their designs. We are going to have to extend our deadline again as we haven't had an opportunity to review all of the designs properly and provide feedback.

Target Market(s)

Accountants and Accounting Firms (mid tier firms)

Industry/Entity Type

Management Consulting

Font styles to use
Other font styles liked:
• Calibri & Attached font files.

Colors
0455a3
3277b5
ffffff

Requirements
Must have
• A Professional A4 double sided colour flyer consisting of:
• Front Page:
• - hero image (attached)
• - Draft content front (attached)
• - Vondra-x Logo (attached)
• Back Page
• - Draft content back (attached)

```html
<!DOCTYPE html>
<html lang="en">
<head>
<meta charset="utf-8">
<title>Vondra-x Accounting Industry Flyer</title>
<link href="https://fonts.googleapis.com/css2?family=Open+Sans:wght@400;600;700&family=Roboto:wght@700;900&display=swap" rel="stylesheet">
<style>
  :root{
    --brand-blue:#0455a3;
    --mid-blue:#3277b5;
    --deep-blue:#1f4393;
    --panel-blue:#1b5fb3;
    --sky-blue:#8fbfe6;
    --ink:#1c1c1c;
    --white:#ffffff;
    --back-text:#d9e3f5;
  }
  *{margin:0;padding:0;box-sizing:border-box}
  html,body{width:1200px;height:1000px;overflow:hidden}
  body{
    position:relative;
    background:linear-gradient(120deg,#7a7a7a 0%,#d6d6d6 30%,#f2f2f2 55%,#ffffff 100%);
    font-family:"Open Sans",Arial,sans-serif;
    color:var(--ink);
  }
  .page{position:absolute;left:280px;width:641px;height:455px;overflow:hidden}
  .page--front{top:35px;background:var(--white)}
  .page--back{top:512px;background:linear-gradient(160deg,#23509f 0%,var(--deep-blue) 60%,#1c3d8a 100%)}
  .front-shapes{position:absolute;inset:0}
  .brand-name{
    position:absolute;left:415px;top:46px;
    font-family:"Open Sans",Arial,sans-serif;font-weight:400;font-size:34px;
    color:var(--white);letter-spacing:.5px;
  }
  .section-title{
    position:absolute;left:35px;top:229px;
    font-family:"Roboto",Arial,sans-serif;font-weight:900;font-size:22px;color:var(--white);
  }
  .service{position:absolute;width:260px}
  .service__icon{position:absolute;left:-25px;top:-2px;width:18px;height:18px;border-radius:50%;background:var(--brand-blue)}
  .service__icon::after{content:"";position:absolute;left:5px;top:5px;width:8px;height:8px;border:1.5px solid var(--white);border-radius:2px}
  .service__title{font-family:"Roboto",Arial,sans-serif;font-weight:700;font-size:12px;color:var(--ink);margin-bottom:3px}
  .service__text{font-size:9.3px;line-height:12.5px;color:#333}
  .contact{position:absolute;left:362px;top:403px;font-size:9.3px;line-height:11px;color:#222}
  .col{position:absolute;color:var(--back-text);font-size:7.2px;line-height:10.4px}
  .col p{margin-bottom:10px;text-align:justify}
  .col h2{font-family:"Roboto",Arial,sans-serif;font-weight:700;font-size:10.5px;color:var(--white);margin:0 0 6px}
  .col ul{list-style:none;margin-bottom:10px}
  .col li::before{content:"• "}
  .col--left{left:26px;top:24px;width:192px}
  .col--right{left:233px;top:24px;width:384px}
  .cta-box{
    position:absolute;left:0;bottom:0;width:215px;height:70px;background:var(--panel-blue);
    color:var(--back-text);font-size:7.2px;line-height:10.4px;text-align:right;padding:16px 9px 0 0;
  }
</style>
</head>
<body>

<section class="page page--front">
  <svg class="front-shapes" width="641" height="455" viewBox="0 0 641 455">
    <defs>
      <linearGradient id="heroTone" x1="0" y1="0" x2="1" y2="1">
        <stop offset="0" stop-color="#3d4a5e"/>
        <stop offset=".5" stop-color="#8b9bb0"/>
        <stop offset="1" stop-color="#2c3a52"/>
      </linearGradient>
    </defs>
    <polygon points="325,0 641,0 641,262 492,262" fill="var(--brand-blue)"/>
    <polygon points="306,0 318,0 486,262 474,262" fill="var(--mid-blue)"/>
    <polygon role="img" aria-label="Hero image: businessman touching a cloud icon surrounded by a network of technology icons" points="0,0 296,0 462,262 0,262" fill="url(#heroTone)"/>
    <polygon points="0,0 180,0 150,14 0,14" fill="var(--brand-blue)"/>
    <rect x="0" y="227" width="180" height="35" fill="var(--brand-blue)"/>
    <polygon points="180,227 195,227 180,262" fill="var(--brand-blue)"/>
    <polygon points="0,262 30,262 185,455 0,455" fill="var(--sky-blue)"/>
    <polygon points="332,430 641,430 641,455 350,455" fill="var(--brand-blue)"/>
  </svg>

  <div class="brand-name">Vondra-x</div>
  <h1 class="section-title">What we do</h1>

  <div class="service" style="left:58px;top:274px">
    <span class="service__icon"></span>
    <div class="service__title">Project Management</div>
    <div class="service__text">Delivering High Quality Projects on time and<br>within budged.</div>
  </div>
  <div class="service" style="left:60px;top:327px">
    <span class="service__icon"></span>
    <div class="service__title">Business Proses Management</div>
    <div class="service__text">Building innovative links between your departments. driving collaboration and providing holistic business solutions</div>
  </div>
  <div class="service" style="left:59px;top:390px">
    <span class="service__icon"></span>
    <div class="service__title">Change Management</div>
    <div class="service__text">Building engagement through business understanding, clear communication and relevant capabilitty.</div>
  </div>
  <div class="service" style="left:357px;top:285px">
    <span class="service__icon"></span>
    <div class="service__title">Business Analysis</div>
    <div class="service__text">Engaging your people to understand current practices and develop smarter business processes</div>
  </div>
  <div class="service" style="left:357px;top:339px">
    <span class="service__icon"></span>
    <div class="service__title">Business Intelligence</div>
    <div class="service__text">Leveraging one of your organisations most valuable assets - your data.</div>
  </div>

  <div class="contact">contact us :<br>(+61) 3 9471 226 or visit www.vondra-x.com.au</div>
</section>

<section class="page page--back">
  <div class="col col--left">
    <h2>Who are Vondra-x?</h2>
    <p>Based in Melbourne, Australia, Vondra-x is a management consulting organisation who partner with their clients to lead the execution of strategic process and system improvement initiatives. Our core purpose is to help your business navigate transformational change through clear and focused execution and enablement.</p>
    <p>Vondra-x has proven experience leading change and delivering improvements to organisations across a range of industries. However, we specialise in working with accounting firms in the middle market helping them to navigate the disruptive changes rapidly changing the face of their industry. Our expertise includes business process automation and the management of onshore and offshore teams across tax and audit compliance services.</p>
    <h2>What are our capabilities?</h2>
    <p>We offer a range of project advisory services including project management, business process improvement, change management, business analysis and business intelligence. At Vondra-x we aim to build your organisation's capabilities enabling you to manage and execute change initiatives. We do this by providing hands-on project delivery along with coaching in best practice project methodologies. We look to establish simple repeatable project and change management processes that can continue to be utilised by your organisation long into the future.</p>
  </div>

  <div class="col col--right">
    <h2>What are the major challenges facing the accounting industry?</h2>
    <p>The three major disruptors facing accounting firms are the offshoring of compliance activities, rapid changes in technology and the internet. These industry wide disruptors are placing pressure on fee negotiations, revenue generation and are also providing a significant increase in competitive activity. As clients continue to push prices down, accounting firms have and/or are in the process of implementing systems and technologies to drive further efficiencies and reduce costs. In addition the outsourcing of accounting services for low end and non-confidential work to further lower client costs has been pervasive. This has now started to extend across end to end tax and audit compliance processes as firms start to recognise the qualified accounting capability they have available to them at a much lower cost.</p>
    <p>The need to win new business and increased competition has resulted in the entry of the Big 4 into the middle tier market and the emergence and expansion of non-traditional competitors with different business models. Cloud computing is enabling businesses to scale at a very rapid rate and maintain low cost operating models. As the industry becomes hyper-competitive it is crucial for accounting firms to deepen their understanding of clients and build their capability to offer value added advisory services.</p>
    <h2>How we can help professional services firms in the accounting industry</h2>
    <p>Vondra-x have deep industry experience gained across the Big 4 and mid-tier accounting firms and a consistent track record for leading change and delivering improvements to business processes. Our people have extensive industry experience leading and managing teams at organisations such as Harlow Brandt, Ellery Voss, QRM Group, Tallis Accountants, Meridale Advisers and Corwen Partners.</p>
    <p style="margin-bottom:2px">Our delivery model involves us working directly alongside you helping you to:</p>
    <ul>
      <li>Recognise the major disruptors for your business</li>
      <li>Ensure you have developed a clear strategy on how to respond</li>
      <li>Develop a plan and execute the changes required to ensure business growth is maintained<br>&nbsp;&nbsp;and the quality of your client work is not compromised</li>
    </ul>
    <h2>Case Study</h2>
    <p>A leading mid-tier accounting firm required support to implement large scale process and system improvements identified through a major organisational review. Through a structured program delivery approach we harnessed the required internal resources, engaged widely across the organisation and delivered major changes throughout the firm every 8 weeks with minimal disruption to normal business operations. The implementation of these improvements freed up over x hours per annum that could be redirected to value added advisory services.</p>
  </div>

  <div class="cta-box">Check out our website at www.vondra-x.com.au<br>and contact us on (+61) 3 9471 226<br>to help your organisation navigate change and<br>drive successful business outcomes.</div>
</section>

</body>
</html>
```